" buscamos elaborar produtos saudáveis, isentos de glúten, lactose e açúcar. E utilizando ingredientes benéficos a nossa saúde, como fibra e gorduras boas (insaturadas). "

```html
<!DOCTYPE html>
<html lang="pt-BR">
<head>
<meta charset="utf-8">
<title>Semente Viva – Tag</title>
<link rel="stylesheet" href="https://fonts.googleapis.com/css2?family=Nunito:wght@600;700&family=Open+Sans:wght@400;600&display=swap">
<style>
  :root {
    --bg: #e9e6e1;
    --tag-white: #ffffff;
    --leaf-light: #eeeeee;
    --leaf-mid: #e2e2e2;
    --brand-green: #7cb342;
    --brand-orange: #f08a24;
    --tag-green: #6a9a22;
    --tag-green-dark: #5e8c1c;
    --text-light: #ffffff;
  }
  * { box-sizing: border-box; margin: 0; padding: 0; }
  html, body { width: 1200px; height: 1200px; overflow: hidden; }
  body {
    background: var(--bg);
    position: relative;
    font-family: "Open Sans", Arial, sans-serif;
  }
  .tag {
    position: absolute;
    left: 160px;
    width: 880px;
    height: 440px;
    border-radius: 220px / 200px;
    overflow: hidden;
    box-shadow: 0 10px 28px rgba(0,0,0,0.12);
  }
  .tag-hole {
    position: absolute;
    right: 46px;
    top: 50%;
    width: 44px;
    height: 44px;
    margin-top: -22px;
    border-radius: 50%;
    background: var(--bg);
    box-shadow: inset 0 2px 4px rgba(0,0,0,0.25);
  }
  .tag-front { top: 110px; background: var(--tag-white); }
  .leaf-decoration {
    position: absolute;
    left: 0; top: 0;
    width: 460px; height: 440px;
    background: radial-gradient(ellipse at 40% 45%, var(--leaf-mid) 0%, var(--leaf-light) 45%, rgba(255,255,255,0) 75%);
  }
  .brand {
    position: absolute;
    left: 290px;
    top: 100px;
    width: 440px;
    text-align: center;
  }
  .brand-mark {
    width: 130px; height: 130px;
    margin: 0 auto 26px;
    border-radius: 50%;
    background: var(--brand-orange);
  }
  .brand-name {
    font-family: "Nunito", Arial, sans-serif;
    font-weight: 700;
    font-size: 62px;
    letter-spacing: 0.5px;
    color: var(--brand-green);
  }
  .tag-back { top: 650px; background: var(--tag-green); }
  .contact-list {
    position: absolute;
    left: 230px;
    top: 92px;
    list-style: none;
  }
  .contact-item {
    display: flex;
    align-items: center;
    height: 52px;
    color: var(--text-light);
    font-size: 29px;
  }
  .contact-item:first-child { padding-left: 40px; }
  .contact-item:nth-child(2) { padding-left: 20px; }
  .contact-item:nth-child(3) { padding-left: 40px; }
  .contact-item:nth-child(4) { padding-left: 0; }
  .contact-item:nth-child(5) { padding-left: 80px; }
  .contact-icon {
    width: 30px; height: 30px;
    margin-right: 20px;
    flex: none;
    border-radius: 4px;
    background: var(--text-light);
    display: flex; align-items: center; justify-content: center;
    color: var(--tag-green);
    font-weight: 600;
    font-size: 22px;
  }
  .contact-icon svg { width: 22px; height: 22px; }
</style>
</head>
<body>
  <section class="tag tag-front">
    <div class="leaf-decoration" role="img" aria-label="Faint decorative leaves and branches"></div>
    <div class="brand">
      <div class="brand-mark"></div>
      <div class="brand-name">Semente Viva</div>
    </div>
    <div class="tag-hole"></div>
  </section>

  <section class="tag tag-back">
    <ul class="contact-list">
      <li class="contact-item">
        <span class="contact-icon">
          <svg viewBox="0 0 24 24"><rect x="7" y="2" width="10" height="20" rx="2" fill="none" stroke="#6a9a22" stroke-width="2.2"/><circle cx="12" cy="18" r="1.3" fill="#6a9a22"/></svg>
        </span>21 90000-1234
      </li>
      <li class="contact-item"><span class="contact-icon">@</span>sementeviva@mail.com</li>
      <li class="contact-item">
        <span class="contact-icon">
          <svg viewBox="0 0 24 24"><circle cx="12" cy="12" r="8" fill="none" stroke="#6a9a22" stroke-width="2"/><path d="M4 12h16M12 4c3 3 3 13 0 16M12 4c-3 3-3 13 0 16" fill="none" stroke="#6a9a22" stroke-width="1.6"/></svg>
        </span>www.sementeviva.com.br
      </li>
      <li class="contact-item"><span class="contact-icon"></span>www.social.com/sementeviva</li>
      <li class="contact-item"><span class="contact-icon"></span>sementeviva</li>
    </ul>
    <div class="tag-hole"></div>
  </section>
</body>
</html>
```